Poster for a Boat show

We need a poster for a boat show. Motorboats and Sailboats is presented in this Boat show (and other nautical topics like diving, wakeboard, kite, surf, fishing, ...)
This boat show is annual and the Poster is for the 2014 edition.

The style must be modern, dynamic.

Important Content:
Name of the boat show: Salon nautique des Brisants
Place: Halle VTR - Gare de Pirlou
Date: 7, 8 et 9 novembre 2014
Website: www.expo-flotvane.ch
Entrée gratuite • Restauration sur place
Please, leave a zone in the poster for sponsors logos

Secondary content (schedule):
07.11.2014 from 17h to 21h
08.11.2014 from 10h to 20h
09.11.2014 from 10h to 18h

It's necessary for us to have the source file (vector) for make, later, the different format (flyers, website, ...)

Exemple of design of other boat show:
http://www.exemple-revue-a.net/images/affiche-a.jpg
http://www.exemple-blog-b.com/images/affiche-b.jpg
http://www.exemple-hotel-c.com/images/affiche-c.jpg
http://www.exemple-port-d.com/images/affiche-d.jpg
http://www.exemple-folio-e.fr/images/affiche-e.png
http://www.exemple-info-f.fr/images/affiche-f.jpg
http://www.exemple-blog-g.com/images/affiche-g.jpg
http://www.exemple-surf-h.com/images/affiche-h.jpg
http://www.exemple-revue-i.net/images/affiche-i.jpeg

Target Market(s)

Nautical enthusiasts, more masculine, high income

Industry/Entity Type

Nautical

Font styles to use
Serif
Sans Serif

Requirements
Must have
• Motor and Sail boat approach

```html
<!DOCTYPE html>
<html lang="fr">
<head>
<meta charset="utf-8">
<title>Salon nautique des Brisants 2014</title>
<link rel="stylesheet" href="https://fonts.googleapis.com/css2?family=Arimo:wght@700&family=Roboto:wght@100;300;400&display=swap">
<style>
  :root {
    --title-indigo: #2b2f8e;
    --sea-top: #2f9ad6;
    --sea-mid: #1f8fd2;
    --sea-deep: #1b78c0;
    --band-blue: #1766b0;
    --sand: #5aa6cf;
    --paper: #ffffff;
    --date-pale: #d7e7f5;
    --year-pale: rgba(214, 232, 246, 0.72);
    --badge-orange: #f7941d;
    --badge-red: #c1272d;
    --badge-edge: #1d1d1b;
  }
  html, body {
    margin: 0;
    padding: 0;
    width: 848px;
    height: 1200px;
    overflow: hidden;
    background: var(--paper);
  }
  .poster { display: block; width: 848px; height: 1200px; }
  .title { font-family: "Arimo", Arial, sans-serif; font-weight: 700; fill: var(--title-indigo); }
  .venue { font-family: "Arimo", Arial, sans-serif; font-weight: 700; fill: var(--paper); }
  .dates { font-family: "Arimo", Arial, sans-serif; font-weight: 700; fill: var(--date-pale); }
  .year { font-family: "Roboto", Helvetica, sans-serif; font-weight: 100; fill: var(--year-pale); }
  .schedule { font-family: "Roboto", Helvetica, sans-serif; font-weight: 400; fill: var(--paper); font-size: 13px; }
  .website { font-family: "Roboto", Helvetica, sans-serif; font-weight: 300; fill: var(--paper); font-size: 32px; }
  .badge-text { font-family: "Arimo", Arial, sans-serif; font-weight: 700; fill: var(--paper); }
  .badge-orange { fill: var(--badge-orange); }
  .badge-red { fill: var(--badge-red); }
  .badge-ring { fill: none; stroke: var(--badge-edge); stroke-width: 1.6; stroke-dasharray: 5 3; }
</style>
</head>
<body>
<svg class="poster" viewBox="0 0 848 1200" xmlns="http://www.w3.org/2000/svg">
  <defs>
    <linearGradient id="sea-gradient" x1="0" y1="0" x2="0" y2="1">
      <stop offset="0" stop-color="#3aa3dc"/>
      <stop offset="0.35" stop-color="var(--sea-mid)"/>
      <stop offset="1" stop-color="var(--sea-deep)"/>
    </linearGradient>
    <linearGradient id="seabed-gradient" x1="0" y1="0" x2="0" y2="1">
      <stop offset="0" stop-color="var(--band-blue)"/>
      <stop offset="0.45" stop-color="#2a7fbf"/>
      <stop offset="1" stop-color="var(--sand)"/>
    </linearGradient>
    <filter id="badge-shadow" x="-20%" y="-20%" width="140%" height="140%">
      <feDropShadow dx="2" dy="3" stdDeviation="3" flood-color="#000" flood-opacity="0.35"/>
    </filter>
  </defs>

  <!-- Underwater backdrop -->
  <rect class="backdrop" role="img" aria-label="Vue sous-marine d'une eau bleue avec rose des vents en filigrane" x="0" y="0" width="848" height="843" fill="url(#sea-gradient)"/>
  <rect class="seabed" role="img" aria-label="Fond marin sablonneux sous l'eau" x="0" y="843" width="848" height="260" fill="url(#seabed-gradient)"/>

  <!-- Sponsor area -->
  <path class="sponsor-zone" d="M0 1058 C 120 1070, 260 1086, 420 1080 C 580 1074, 720 1050, 848 1056 L 848 1200 L 0 1200 Z" fill="var(--paper)"/>

  <!-- Title -->
  <text class="title" x="168" y="159" font-size="154" textLength="520" lengthAdjust="spacingAndGlyphs">SALON</text>
  <text class="title" x="170" y="281" font-size="100" textLength="510" lengthAdjust="spacingAndGlyphs">NAUTIQUE</text>
  <text class="title" x="170" y="375" font-size="78" textLength="510" lengthAdjust="spacingAndGlyphs">DES BRISANTS</text>

  <!-- Venue -->
  <text class="venue" x="170" y="430" font-size="29" textLength="525" lengthAdjust="spacingAndGlyphs">HALLE VTR - GARE DE PIRLOU</text>

  <!-- Dates -->
  <text class="dates" x="235" y="530" font-size="100" textLength="407" lengthAdjust="spacingAndGlyphs">7, 8 et 9</text>
  <text class="dates" x="170" y="625" font-size="104" textLength="525" lengthAdjust="spacingAndGlyphs">novembre</text>
  <text class="year" x="146" y="838" font-size="268" textLength="534" lengthAdjust="spacingAndGlyphs">2014</text>

  <!-- Schedule -->
  <text class="schedule" x="432" y="869" text-anchor="middle">07.11.2014 FROM 17H TO 21H</text>
  <text class="schedule" x="432" y="895" text-anchor="middle">08.11.2014 FROM 10H TO 20H</text>
  <text class="schedule" x="432" y="920" text-anchor="middle">09.11.2014 FROM 10H TO 18H</text>

  <!-- Website -->
  <text class="website" x="437" y="960" text-anchor="middle">www.expo-flotvane.ch</text>

  <!-- Free entry badge -->
  <g class="badge badge-free-entry" transform="translate(731 207) rotate(14)">
    <circle class="badge-orange" r="66" filter="url(#badge-shadow)"/>
    <circle class="badge-ring" r="65"/>
    <text class="badge-text" y="-20" font-size="19" text-anchor="middle">Entrée</text>
    <text class="badge-text" y="2" font-size="19" text-anchor="middle">gratuite</text>
    <text class="badge-text" y="24" font-size="18" text-anchor="middle">(free entry)</text>
  </g>

  <!-- On-site catering badge -->
  <g class="badge badge-catering" transform="translate(111 497) rotate(-14)">
    <circle class="badge-red" r="69" filter="url(#badge-shadow)"/>
    <circle class="badge-ring" r="68"/>
    <text class="badge-text" y="-27" font-size="16" text-anchor="middle">Restauration</text>
    <text class="badge-text" y="-8" font-size="16" text-anchor="middle">sur place</text>
    <text class="badge-text" y="11" font-size="16" text-anchor="middle">(on-site</text>
    <text class="badge-text" y="30" font-size="16" text-anchor="middle">catering)</text>
  </g>
</svg>
</body>
</html>
```